Dog Walking logo design

Dog Walking, Dog Sitting, Pet Taxi, Doggy Day Care. I'm looking for a design that shows a man walking 3 dogs. The dogs are on leads and we only see the mans legs. I'm open to suggestion re: the image of a sole of a boot associated with walking. I would like my company name as part of or incorporated into any image or logo.

Industry/Entity Type

It Company

Contact Information for Business Card

Fernhill Pet Rambles
Contact: www.fernhillrambles.example
Tel: 07912 358264

```html
<!DOCTYPE html>
<html lang="en">
<head>
<meta charset="utf-8">
<title>Fernhill Pet Rambles – Business Card</title>
<link href="https://fonts.googleapis.com/css2?family=Open+Sans:wght@400;600;700&display=swap" rel="stylesheet">
<style>
  :root {
    --green: #138a4c;
    --green-deep: #0b6e39;
    --green-light: #2fa86a;
    --white: #ffffff;
    --paper: #f4f5f4;
    --ink: #2b2b2b;
    --backdrop: #e9e7e2;
  }
  * { box-sizing: border-box; margin: 0; padding: 0; }
  html, body { width: 1200px; height: 1023px; overflow: hidden; }
  body {
    background: var(--backdrop);
    font-family: "Open Sans", Arial, sans-serif;
    display: flex;
    flex-direction: column;
    align-items: center;
    justify-content: center;
    gap: 70px;
  }
  .card {
    width: 560px;
    height: 320px;
    position: relative;
    box-shadow: 0 10px 26px rgba(0,0,0,.18);
    overflow: hidden;
  }

  /* Front */
  .card-front { background: linear-gradient(135deg, var(--white), var(--paper)); }
  .front-band {
    position: absolute; left: 0; right: 0; bottom: 0; height: 26px;
    background: var(--green);
  }
  .front-divider {
    position: absolute; left: 250px; top: 0; bottom: 26px; width: 2px;
    background: var(--green);
  }
  .front-rule {
    position: absolute; left: 250px; right: 0; top: 150px; height: 2px;
    background: var(--green);
  }
  .brand {
    position: absolute; left: 26px; top: 28px;
    display: flex; align-items: center; gap: 12px;
  }
  .brand-square { width: 64px; height: 64px; background: var(--green); }
  .brand-name {
    color: var(--green); font-size: 17px; font-weight: 600; line-height: 1.2; width: 130px;
  }
  .identity { position: absolute; left: 280px; top: 78px; }
  .identity-name { color: var(--green); font-size: 26px; font-weight: 700; line-height: 1.1; }
  .identity-role { color: var(--ink); font-size: 18px; font-weight: 400; margin-top: 2px; }
  .contacts {
    position: absolute; left: 280px; top: 172px;
    list-style: none; color: var(--ink); font-size: 12.5px; line-height: 1.45;
  }
  .contacts li { display: flex; align-items: flex-start; gap: 8px; }
  .contacts svg { flex: none; margin-top: 3px; }

  /* Back */
  .card-back {
    background: linear-gradient(125deg, var(--green-deep) 0%, var(--green) 55%, var(--green-light) 100%);
    display: flex; align-items: center; justify-content: center;
  }
  .back-brand { display: flex; align-items: center; gap: 22px; }
  .back-square { width: 120px; height: 120px; background: var(--white); }
  .back-name {
    color: var(--white); font-size: 30px; font-weight: 600; line-height: 1.2; width: 230px;
  }
</style>
</head>
<body>

  <section class="card card-front" aria-label="Business card front">
    <div class="brand">
      <div class="brand-square"></div>
      <div class="brand-name">Fernhill Pet Rambles</div>
    </div>
    <div class="front-divider"></div>
    <div class="identity">
      <div class="identity-name">Your Name</div>
      <div class="identity-role">Your Position</div>
    </div>
    <div class="front-rule"></div>
    <ul class="contacts">
      <li>
        <svg width="11" height="11" viewBox="0 0 12 12"><rect width="12" height="12" rx="2" fill="#138a4c"/><path d="M4 3l1.2 1.6-.7.8a4 4 0 0 0 2.1 2.1l.8-.7L9 8l-.6 1C5.6 9 3 6.4 3 3.6z" fill="#fff"/></svg>
        <span>07912 358264</span>
      </li>
      <li>
        <svg width="11" height="11" viewBox="0 0 12 12"><rect width="12" height="12" rx="2" fill="#138a4c"/><circle cx="6" cy="6" r="3.2" fill="none" stroke="#fff" stroke-width="1"/><path d="M2.8 6h6.4M6 2.8v6.4" stroke="#fff" stroke-width=".8"/></svg>
        <span>www.fernhillrambles.example</span>
      </li>
      <li>
        <svg width="11" height="11" viewBox="0 0 12 12"><rect width="12" height="12" rx="2" fill="#138a4c"/><rect x="2.5" y="3.5" width="7" height="5" fill="none" stroke="#fff" stroke-width=".9"/><path d="M2.5 3.5 6 6.4 9.5 3.5" fill="none" stroke="#fff" stroke-width=".9"/></svg>
        <span>hello07@fernmail.example</span>
      </li>
      <li>
        <svg width="11" height="11" viewBox="0 0 12 12"><rect width="12" height="12" rx="2" fill="#138a4c"/><path d="M6 2.3a2.6 2.6 0 0 0-2.6 2.6C3.4 7 6 9.7 6 9.7S8.6 7 8.6 4.9A2.6 2.6 0 0 0 6 2.3z" fill="#fff"/><circle cx="6" cy="4.9" r=".9" fill="#138a4c"/></svg>
        <span>12 Orchard Row, Mill Lane, Ashby Green,<br>Northfield, NF4 2QT</span>
      </li>
    </ul>
    <div class="front-band"></div>
  </section>

  <section class="card card-back" aria-label="Business card back">
    <div class="back-brand">
      <div class="back-square"></div>
      <div class="back-name">Fernhill Pet Rambles</div>
    </div>
  </section>

</body>
</html>
```